Design for Certificate

Design a certificate for training, providing our company logo such as attachments. Company's name is "BRYNE Fjellvik Advisory Ltd", please refer to our company profile: https://www.bryne-fjellvik.example/company_info

The style of the current certificate is also attached, and another certificate of another company can be referred to. Psd & jpg are required for the final draft (the layers of psd are not merged). Thanks!

```html
<!DOCTYPE html>
<html lang="en">
<head>
<meta charset="utf-8">
<title>Certificate of Completion – BRYNE Fjellvik</title>
<link href="https://fonts.googleapis.com/css2?family=Josefin+Sans:wght@500;600;700&family=Playfair+Display:wght@400&display=swap" rel="stylesheet">
<style>
  :root {
    --paper: #fbe7d8;
    --paper-light: #fdeee2;
    --band-warm: #f6d9b8;
    --band-cream: #fbe8c4;
    --gold: #c59a3a;
    --gold-light: #dfb65a;
    --gold-soft: #d6ab4c;
  }
  * { margin: 0; padding: 0; box-sizing: border-box; }
  html, body { width: 1200px; height: 848px; overflow: hidden; background: var(--paper); }
  .certificate {
    position: relative;
    width: 1200px; height: 848px;
    overflow: hidden;
    background:
      linear-gradient(125deg, var(--band-cream) 0%, transparent 14%),
      linear-gradient(118deg, transparent 0%, rgba(246,217,184,.55) 10%, transparent 32%),
      linear-gradient(300deg, rgba(247,208,150,.55) 0%, transparent 22%),
      linear-gradient(318deg, transparent 12%, rgba(240,210,180,.5) 26%, transparent 40%),
      linear-gradient(180deg, var(--paper-light), var(--paper));
    color: var(--gold);
  }
  .frame { position: absolute; inset: 0; }
  .text { position: absolute; left: 0; width: 1200px; text-align: center; }
  .sans { font-family: "Josefin Sans", sans-serif; font-weight: 600; }
  .serif { font-family: "Playfair Display", serif; font-weight: 400; text-transform: uppercase; }
  .title-main { top: 44px; font-size: 84px; line-height: 1; letter-spacing: 1px; color: var(--gold-light); }
  .title-sub { top: 118px; font-size: 44px; line-height: 1; letter-spacing: 1px; color: var(--gold); }
  .kicker { font-size: 17px; letter-spacing: 6px; color: var(--gold-soft); }
  .awarded { top: 212px; }
  .recipient { top: 250px; font-size: 66px; line-height: 1; letter-spacing: 2px; color: var(--gold); }
  .completed { top: 372px; }
  .course { top: 406px; font-size: 41px; line-height: 38px; letter-spacing: .5px; color: var(--gold); }
  .details { top: 502px; }
  .details .date { font-family: "Josefin Sans", sans-serif; font-weight: 600; font-size: 22px; letter-spacing: 0; color: var(--gold-light); margin-left: 8px; }
  .label { position: absolute; font-size: 16px; letter-spacing: 4px; line-height: 19px; text-align: center; color: var(--gold-soft); }
  .cert-no { left: 196px; width: 260px; top: 722px; }
  .signatory { left: 756px; width: 260px; top: 722px; }
  .signature {
    position: absolute; left: 754px; top: 640px; width: 256px; height: 62px;
    background: linear-gradient(90deg, rgba(223,182,90,.15), rgba(223,182,90,.45), rgba(223,182,90,.15));
    border-radius: 30px;
  }
  .brand-mark {
    position: absolute; left: 520px; top: 590px; width: 160px;
    text-align: center; font-size: 22px; line-height: 28px; letter-spacing: 2px; color: var(--gold-light);
  }
  .brand-mark .square { display: block; width: 26px; height: 26px; margin: 0 auto 14px; border: 2px solid var(--gold-light); }
  .footer-name { top: 784px; font-size: 20px; letter-spacing: 7px; color: var(--gold-light); }
</style>
</head>
<body>
<main class="certificate">
  <svg class="frame" width="1200" height="848" viewBox="0 0 1200 848" aria-hidden="true">
    <g fill="none" stroke="#dfb65a">
      <!-- thick outer frame -->
      <g stroke-width="5">
        <polyline points="265,58 66,58 66,800 480,800"/>
        <polyline points="942,58 1137,58 1137,800 722,800"/>
      </g>
      <!-- inner thin frame -->
      <g stroke-width="1.5">
        <polyline points="265,70 81,70 81,787 480,787"/>
        <polyline points="942,70 1124,70 1124,787 722,787"/>
        <!-- corner squares -->
        <rect x="40" y="31" width="56" height="54"/>
        <rect x="1105" y="31" width="56" height="54"/>
        <rect x="40" y="763" width="56" height="55"/>
        <rect x="1105" y="763" width="56" height="55"/>
        <!-- corner tick lines -->
        <line x1="96" y1="85" x2="158" y2="85"/><line x1="96" y1="85" x2="96" y2="148"/>
        <line x1="1105" y1="85" x2="1043" y2="85"/><line x1="1105" y1="85" x2="1105" y2="148"/>
        <line x1="96" y1="763" x2="158" y2="763"/><line x1="96" y1="763" x2="96" y2="700"/>
        <line x1="1105" y1="763" x2="1043" y2="763"/><line x1="1105" y1="763" x2="1105" y2="700"/>
        <!-- rule lines -->
        <line x1="290" y1="312" x2="910" y2="312"/>
        <line x1="675" y1="531" x2="934" y2="531"/>
        <line x1="196" y1="707" x2="456" y2="707"/>
        <line x1="756" y1="707" x2="1016" y2="707"/>
      </g>
    </g>
    <g fill="#dfb65a">
      <rect x="155" y="82" width="5" height="5" transform="rotate(45 157.5 84.5)"/>
      <rect x="93" y="146" width="5" height="5" transform="rotate(45 95.5 148.5)"/>
      <rect x="1040" y="82" width="5" height="5" transform="rotate(45 1042.5 84.5)"/>
      <rect x="1102" y="146" width="5" height="5" transform="rotate(45 1104.5 148.5)"/>
      <rect x="155" y="760" width="5" height="5" transform="rotate(45 157.5 762.5)"/>
      <rect x="93" y="698" width="5" height="5" transform="rotate(45 95.5 700.5)"/>
      <rect x="1040" y="760" width="5" height="5" transform="rotate(45 1042.5 762.5)"/>
      <rect x="1102" y="698" width="5" height="5" transform="rotate(45 1104.5 700.5)"/>
      <rect x="288" y="310" width="4" height="4" transform="rotate(45 290 312)"/>
      <rect x="908" y="310" width="4" height="4" transform="rotate(45 910 312)"/>
      <rect x="673" y="529" width="4" height="4" transform="rotate(45 675 531)"/>
      <rect x="932" y="529" width="4" height="4" transform="rotate(45 934 531)"/>
      <rect x="194" y="705" width="4" height="4" transform="rotate(45 196 707)"/>
      <rect x="454" y="705" width="4" height="4" transform="rotate(45 456 707)"/>
      <rect x="754" y="705" width="4" height="4" transform="rotate(45 756 707)"/>
      <rect x="1014" y="705" width="4" height="4" transform="rotate(45 1016 707)"/>
    </g>
  </svg>

  <h1 class="text sans title-main">CERTIFICATE</h1>
  <h2 class="text sans title-sub">OF COMPLETION</h2>

  <p class="text serif kicker awarded">This certificate is awarded to</p>
  <p class="text sans recipient">JOHN DOE</p>

  <p class="text serif kicker completed">Has successfully completed</p>
  <p class="text sans course">BRAND REPUTATION MANAGEMENT<br>TRAINING COURSE</p>
  <p class="text serif kicker details">Sixteen hours, held on<span class="date">NOVEMBER 10, 2019</span></p>

  <div class="brand-mark sans"><span class="square"></span>BRYNE<br>FJELLVIK</div>

  <div class="signature" role="img" aria-label="Handwritten signature of the Chief Technology Officer"></div>

  <p class="label serif cert-no">Certificate No.</p>
  <p class="label serif signatory">Chief Technology<br>Officer</p>

  <p class="text serif footer-name">Bryne Fjellvik</p>
</main>
</body>
</html>
```